Graphic Design for Company Van - White Marlo Pivot Haulmate 2019 LWB

We are a Electronic Security Systems Company specializing in CCTV, Intruder Alarms, Fire Alarms, Access Control and Gate Automation.
I am looking for a modern design for a van wrap to include company logo, phone number, website, the types of work we do (CCTV ect), and our QLR Licence number, its specifically for the model of van in the project name mentioned above. I will attach some of our branded signage and siren logo with some more details. thank you.

```html
<!DOCTYPE html>
<html lang="en">
<head>
<meta charset="utf-8">
<title>Birch Guard – Van Wrap Layouts</title>
<link rel="stylesheet" href="https://fonts.googleapis.com/css2?family=Lato:wght@400;700&family=Poppins:wght@600&family=Roboto+Condensed:wght@700&display=swap">
<style>
  :root {
    --red: #e23b40;
    --red-light: #f1666b;
    --red-dark: #a3161c;
    --red-deep: #7c1015;
    --ink: #1a1a1a;
    --white: #ffffff;
    --paper: #f4f4f4;
    --badge-blue: #1d3f8c;
  }
  html, body {
    margin: 0;
    padding: 0;
    width: 1200px;
    height: 1200px;
    overflow: hidden;
    background: var(--paper);
  }
  .canvas {
    position: relative;
    width: 1200px;
    height: 1200px;
    display: flex;
    flex-direction: column;
    justify-content: space-evenly;
    align-items: center;
  }
  .wrap-layout {
    display: block;
    width: 1120px;
    height: 420px;
    filter: drop-shadow(0 6px 14px rgba(0,0,0,0.12));
  }
  .brand-name { font-family: "Lato", sans-serif; font-weight: 700; fill: var(--ink); }
  .brand-tagline { font-family: "Lato", sans-serif; font-weight: 400; fill: var(--ink); }
  .phone { font-family: "Poppins", sans-serif; font-weight: 600; letter-spacing: 3px; }
  .website { font-family: "Poppins", sans-serif; font-weight: 600; fill: var(--red-dark); }
  .services { font-family: "Roboto Condensed", sans-serif; font-weight: 700; fill: var(--white); }
  .licence-text { font-family: "Lato", sans-serif; font-weight: 400; fill: var(--ink); }
  .licence-strong { font-family: "Lato", sans-serif; font-weight: 700; fill: var(--badge-blue); }
</style>
</head>
<body>
<main class="canvas">

  <!-- Layout A: white base with red sweeps -->
  <svg class="wrap-layout layout-white" viewBox="0 0 1120 420" aria-label="Van side wrap, white layout">
    <rect class="panel-base" x="0" y="0" width="1120" height="420" rx="28" fill="var(--white)"/>
    <clipPath id="panel-a"><rect x="0" y="0" width="1120" height="420" rx="28"/></clipPath>
    <g clip-path="url(#panel-a)">
      <polygon class="sweep-front" points="110,210 360,0 640,0 330,210" fill="var(--red)"/>
      <polygon class="sweep-front-shade" points="330,210 640,0 700,0 400,210" fill="var(--red-dark)"/>
      <polygon class="sweep-lower" points="330,420 540,290 1120,270 1120,420" fill="var(--red)"/>
      <polygon class="sweep-lower-light" points="540,290 1120,270 1120,290 600,302" fill="var(--red-light)"/>
      <polygon class="service-band" points="560,240 1120,220 1120,262 545,282" fill="var(--red-dark)"/>
      <rect class="trim-strip" x="420" y="366" width="600" height="20" rx="6" fill="var(--ink)"/>
    </g>

    <rect class="brand-square" x="700" y="52" width="38" height="38" fill="var(--red)"/>
    <text class="brand-name" x="752" y="88" font-size="46">Birch Guard</text>
    <text class="brand-tagline" x="752" y="124" font-size="25">CCTV &amp; Alarm Installation</text>

    <text class="services" x="572" y="267" font-size="14" textLength="520" lengthAdjust="spacingAndGlyphs" transform="rotate(-2.05 572 267)">CCTV • INTRUDER ALARMS • FIRE ALARMS • ACCESS CONTROL • GATE AUTOMATION</text>

    <g class="service-icons" fill="var(--white)" stroke="var(--red-dark)" stroke-width="3">
      <circle cx="600" cy="326" r="16"/>
      <circle cx="642" cy="325" r="16"/>
      <circle cx="684" cy="324" r="16"/>
      <circle cx="726" cy="323" r="16"/>
    </g>

    <text class="phone" x="300" y="250" font-size="34" fill="var(--ink)">0810005521</text>
    <text class="website" x="300" y="283" font-size="20">www.birchguard.ie</text>

    <g class="licence-badge">
      <circle cx="132" cy="262" r="11" fill="none" stroke="var(--red)" stroke-width="4"/>
      <text class="licence-text" x="150" y="252" font-size="8">Licensed by</text>
      <text class="licence-strong" x="150" y="263" font-size="8.5">The Quality Licensing Regulator</text>
      <text class="licence-text" x="150" y="274" font-size="8">QLR Licence Number 0417</text>
    </g>
  </svg>

  <!-- Layout B: red base with white diagonal -->
  <svg class="wrap-layout layout-red" viewBox="0 0 1120 420" aria-label="Van side wrap, red layout">
    <rect class="panel-base" x="0" y="0" width="1120" height="420" rx="28" fill="var(--red)"/>
    <clipPath id="panel-b"><rect x="0" y="0" width="1120" height="420" rx="28"/></clipPath>
    <g clip-path="url(#panel-b)">
      <polygon class="sweep-top-light" points="500,0 1120,0 1120,30 700,70" fill="var(--red-light)"/>
      <polygon class="diagonal-white" points="0,180 1120,70 1120,170 0,370" fill="var(--white)"/>
      <polygon class="front-white" points="0,180 360,145 240,420 0,420" fill="var(--white)"/>
      <polygon class="service-band" points="330,320 1120,178 1120,222 330,366" fill="var(--red-dark)"/>
      <polygon class="band-edge" points="330,366 1120,222 1120,232 330,376" fill="var(--red-deep)"/>
      <rect class="trim-strip" x="420" y="372" width="600" height="20" rx="6" fill="var(--ink)"/>
    </g>

    <g class="brand-lockup" transform="rotate(-8 690 162)">
      <rect class="brand-square" x="646" y="130" width="34" height="34" fill="var(--red)"/>
      <text class="brand-name" x="692" y="162" font-size="44">Birch Guard</text>
      <text class="brand-tagline" x="700" y="198" font-size="24">CCTV &amp; Alarm Installation</text>
    </g>

    <text class="services" x="400" y="352" font-size="16" transform="rotate(-10.2 400 352)">CCTV • INTRUDER ALARMS • FIRE ALARMS • ACCESS CONTROL • GATE AUTOMATION</text>

    <text class="website" x="258" y="262" font-size="20" transform="rotate(-6 258 262)">www.birchguard.ie</text>
    <text class="phone" x="262" y="300" font-size="32" fill="var(--red-dark)" transform="rotate(-6 262 300)">0810005521</text>

    <g class="licence-badge">
      <circle cx="100" cy="242" r="11" fill="none" stroke="var(--red)" stroke-width="4"/>
      <text class="licence-text" x="118" y="232" font-size="8">Licensed by</text>
      <text class="licence-strong" x="118" y="243" font-size="8.5">The Quality Licensing Regulator</text>
      <text class="licence-text" x="118" y="254" font-size="8">QLR Licence Number 0417</text>
    </g>
  </svg>

</main>
</body>
</html>
```